Product Designer Business Card

Small product design, engineering and prototyping firm in need of a clean, professional business card design. To support our 3D design and drawing services, we offer 3D printing, molding, and casting of plastics, silicones, resins, etc. Our logo can still be modified/changed if necessary. The red/orange color is preferred, but may be substituted with blue or green, potentially. Either way, the colour of the logo should be match/compliment colors used throughout the design. One thought is to have the logo/contact info on one side, with the other side describing services offered, like with a small icon of 3D printer, molding, casting, and computer with a 3D model on-screen.
Industry/Entity Type
Mechanical Engineering
Contact Information for Business Card
Company: Velkin Design
Phone: 613-555-0147
Email: marc@velkindesign.ca

```html
<!DOCTYPE html>
<html lang="en">
<head>
<meta charset="utf-8">
<title>Velkin Design – Business Card</title>
<link href="https://fonts.googleapis.com/css2?family=Orbitron:wght@600&family=Poppins:wght@400;600&display=swap" rel="stylesheet">
<style>
  :root {
    --stage: #2b2b2d;
    --red-deep: #5e0408;
    --red-mid: #9c0a10;
    --red-bright: #d0141b;
    --white: #ffffff;
    --ink: #141414;
    --label-red: #9a1016;
    --icon-tone: #e9e2e2;
  }
  * { box-sizing: border-box; margin: 0; padding: 0; }
  html, body { width: 1200px; height: 880px; overflow: hidden; }
  body {
    background: var(--stage);
    position: relative;
    font-family: "Poppins", sans-serif;
  }
  .card {
    position: absolute;
    top: 285px;
    width: 540px;
    height: 310px;
    border-radius: 16px;
    overflow: hidden;
    box-shadow: 0 10px 30px rgba(0,0,0,.45);
  }
  .card--front { left: 40px; }
  .card--back { left: 620px; }

  .card__ground {
    position: absolute; inset: 0;
    background:
      linear-gradient(135deg, rgba(0,0,0,.25) 0%, transparent 40%),
      radial-gradient(ellipse at 55% 45%, var(--red-bright) 0%, var(--red-mid) 45%, var(--red-deep) 100%);
  }

  /* Front side */
  .brand {
    position: absolute;
    left: 110px; top: 80px;
    display: flex; align-items: center; gap: 14px;
    color: var(--white);
    font-family: "Orbitron", sans-serif;
    font-weight: 600;
    font-size: 34px;
    letter-spacing: 3px;
  }
  .brand__dot {
    width: 34px; height: 34px;
    border-radius: 50%;
    background: var(--white);
  }
  .rule {
    position: absolute;
    left: 36px; right: 36px; top: 214px;
    height: 2px;
    background: var(--white);
  }
  .contact {
    position: absolute;
    color: var(--white);
    font-size: 14px;
  }
  .contact strong { font-weight: 600; }
  .contact--email { right: 40px; top: 186px; }
  .contact--phone { left: 40px; top: 228px; }

  /* Back side */
  .band { position: absolute; inset: 0; }
  .back-title {
    position: absolute;
    left: 0; right: 0; top: 22px;
    text-align: center;
    color: var(--white);
    font-family: "Orbitron", sans-serif;
    font-weight: 600;
    font-size: 32px;
    letter-spacing: 2px;
  }
  .services {
    position: absolute;
    left: 30px; right: 30px; top: 112px;
    display: flex; justify-content: space-around;
  }
  .service {
    display: flex; flex-direction: column; align-items: center; gap: 8px;
  }
  .service__icon {
    width: 92px; height: 92px;
    border-radius: 10px;
    background: linear-gradient(160deg, var(--icon-tone), #cfc6c6);
  }
  .service__label {
    font-family: "Orbitron", sans-serif;
    font-weight: 600;
    font-size: 17px;
    color: var(--label-red);
  }
</style>
</head>
<body>

<section class="card card--front" aria-label="Business card front">
  <div class="card__ground" role="img" aria-label="Red low-poly faceted background"></div>
  <div class="brand"><span class="brand__dot"></span><span class="brand__name">Velkin Design</span></div>
  <p class="contact contact--email"><strong>Email:</strong> marc@velkindesign.ca</p>
  <div class="rule"></div>
  <p class="contact contact--phone"><strong>Phone:</strong> 613-555-0147</p>
</section>

<section class="card card--back" aria-label="Business card back">
  <div class="card__ground" role="img" aria-label="Red low-poly faceted background"></div>
  <svg class="band" viewBox="0 0 540 310" preserveAspectRatio="none" aria-hidden="true">
    <path d="M0 120 C150 96 330 60 540 70 L540 250 C360 240 170 280 0 300 Z" fill="rgba(255,255,255,.35)"/>
    <path d="M0 128 C150 104 330 70 540 80 L540 240 C360 232 170 268 0 290 Z" fill="var(--white)"/>
  </svg>
  <h2 class="back-title">Velkin Design</h2>
  <div class="services">
    <div class="service">
      <div class="service__icon" role="img" aria-label="Line icon of a consultant at a desk with speech bubbles"></div>
      <span class="service__label">Consult</span>
    </div>
    <div class="service">
      <div class="service__icon" role="img" aria-label="Line icon of a monitor with a pen tool and gear"></div>
      <span class="service__label">Design</span>
    </div>
    <div class="service">
      <div class="service__icon" role="img" aria-label="Line icon of a blueprint with pencil and gears"></div>
      <span class="service__label">Prototype</span>
    </div>
  </div>
</section>

</body>
</html>
```